Business card for femtech company

Nothing too elaborate but elegant and geared towards the mother and baby market. Prefer full-bleed with logo (attached) rear.

```html
<!DOCTYPE html>
<html lang="en">
<head>
<meta charset="utf-8">
<title>Nestwell business card</title>
<link rel="stylesheet" href="https://fonts.googleapis.com/css2?family=Montserrat:wght@400;500;700&display=swap">
<style>
  :root {
    --teal: #5bc4b9;
    --white: #ffffff;
    --backdrop: #bdbdbd;
    --shadow: rgba(0, 0, 0, 0.22);
  }
  * { margin: 0; padding: 0; box-sizing: border-box; }
  html, body { width: 1200px; height: 815px; overflow: hidden; }
  body {
    background: var(--backdrop);
    font-family: "Montserrat", sans-serif;
    color: var(--white);
    position: relative;
  }
  .card {
    position: absolute;
    width: 540px;
    height: 309px;
    border-radius: 22px;
    background: var(--teal);
    overflow: hidden;
    box-shadow: 0 10px 24px var(--shadow);
  }
  .card--front { left: 40px; top: 253px; }
  .card--back { left: 620px; top: 253px; }

  .front-accent { position: absolute; inset: 0; }

  .front-details {
    position: absolute;
    left: 34px;
    top: 42px;
  }
  .brand-name {
    font-weight: 400;
    font-size: 44px;
    letter-spacing: 1px;
    line-height: 1;
  }
  .person-name {
    margin-top: 16px;
    font-weight: 700;
    font-size: 19px;
    letter-spacing: 1.5px;
    text-transform: uppercase;
  }
  .person-role {
    font-weight: 400;
    font-size: 11px;
    letter-spacing: 1.5px;
    text-transform: uppercase;
  }
  .address {
    margin-top: 14px;
    font-size: 11px;
    line-height: 1.45;
    font-style: normal;
  }
  .contact-list {
    list-style: none;
    margin-top: 10px;
    font-size: 11px;
    line-height: 1.55;
  }
  .contact-list li { display: flex; align-items: center; gap: 6px; }
  .contact-icon { width: 10px; height: 10px; flex: none; }

  .back-brand {
    position: absolute;
    left: 0; right: 0; top: 0; bottom: 0;
    display: flex;
    align-items: center;
    justify-content: center;
    gap: 22px;
  }
  .back-brand__dot {
    width: 70px; height: 70px;
    border-radius: 50%;
    background: var(--white);
  }
  .back-brand__name {
    font-weight: 400;
    font-size: 64px;
    letter-spacing: 1px;
  }
</style>
</head>
<body>

<section class="card card--front" aria-label="Card front">
  <svg class="front-accent" width="540" height="309" viewBox="0 0 540 309" aria-hidden="true">
    <polygon points="300,0 540,0 540,150 470,309 540,309 540,0" fill="var(--white)"/>
    <polygon points="300,0 540,0 540,120" fill="var(--white)"/>
    <circle cx="430" cy="120" r="82" fill="var(--teal)"/>
    <circle cx="430" cy="120" r="82" fill="none" stroke="var(--white)" stroke-width="10"/>
  </svg>

  <div class="front-details">
    <div class="brand-name">Nestwell</div>
    <div class="person-name">Dana Reyes</div>
    <div class="person-role">Manager</div>
    <address class="address">48 Willow Park Lane<br>Brookfield, MN 55210</address>
    <ul class="contact-list">
      <li>
        <svg class="contact-icon" viewBox="0 0 10 10" aria-hidden="true"><path d="M2 1 L4 3 L3 4 Q4 6 6 7 L7 6 L9 8 L8 9 Q3 9 1 2 Z" fill="var(--white)"/></svg>
        (555)210-4471
      </li>
      <li>
        <svg class="contact-icon" viewBox="0 0 10 10" aria-hidden="true"><rect x="2.5" y="0.5" width="5" height="9" rx="1" fill="none" stroke="var(--white)"/></svg>
        (555)318-92064
      </li>
      <li>
        <svg class="contact-icon" viewBox="0 0 10 10" aria-hidden="true"><rect x="0.5" y="2" width="9" height="6.5" fill="var(--white)"/><path d="M0.5 2 L5 5.5 L9.5 2" fill="none" stroke="var(--teal)"/></svg>
        hello@nestwellcare.com
      </li>
      <li>
        <svg class="contact-icon" viewBox="0 0 10 10" aria-hidden="true"><circle cx="5" cy="5" r="4.3" fill="none" stroke="var(--white)"/><path d="M0.7 5 H9.3 M5 0.7 V9.3" stroke="var(--white)" stroke-width="0.8"/></svg>
        www.nestwellcare.com
      </li>
    </ul>
  </div>
</section>

<section class="card card--back" aria-label="Card back">
  <div class="back-brand">
    <span class="back-brand__dot" aria-hidden="true"></span>
    <span class="back-brand__name">Nestwell</span>
  </div>
</section>

</body>
</html>
```